My business name is Rosalind Mae Design
I wish for a flower or flowers close up in pinks or purple
With my business Name on the front and all rest of the details on the back
I make artificial flower designs , I also make acrylic water designs ,and do my own art work ,I work from home ,

Target Market(s)

Every day people new homes etc

Industry/Entity Type

Business

Font styles to use
Script

Colors
e664a6
b667aa
6b449b

```html
<!DOCTYPE html>
<html lang="en">
<head>
<meta charset="utf-8">
<title>Rosalind Mae Design – Business Card</title>
<link rel="stylesheet" href="https://fonts.googleapis.com/css2?family=Arimo:wght@400&family=Lobster&display=swap">
<style>
  :root {
    --backdrop: #3b3836;
    --card-pink: #f8649a;
    --card-pink-light: #ff79a8;
    --rose-deep: #a3135f;
    --rose-mid: #c8267a;
    --rose-light: #e664a6;
    --bloom-red: #e8174d;
    --bloom-dark: #8e0f33;
    --ink-white: #ffffff;
  }
  * { margin: 0; padding: 0; box-sizing: border-box; }
  html, body {
    width: 1200px;
    height: 800px;
    overflow: hidden;
    background: var(--backdrop);
  }
  .sheet {
    width: 1200px;
    height: 800px;
    display: flex;
    align-items: center;
    justify-content: center;
    gap: 40px;
  }
  .card {
    position: relative;
    width: 550px;
    height: 314px;
    overflow: hidden;
    border-radius: 3px;
    box-shadow: 0 10px 30px rgba(0, 0, 0, 0.35);
  }

  /* Back of card */
  .card--back {
    background: linear-gradient(160deg, var(--card-pink) 0%, var(--card-pink-light) 100%);
  }
  .card--back .bloom {
    position: absolute;
    left: -40px;
    top: 60px;
    width: 260px;
    height: 240px;
    border-radius: 50%;
    background: radial-gradient(circle at 55% 45%, var(--bloom-red) 0%, #c4123f 50%, var(--bloom-dark) 100%);
  }
  .contact-name {
    position: absolute;
    left: 330px;
    top: 72px;
    font-family: "Arimo", Arial, sans-serif;
    font-size: 15px;
    color: var(--ink-white);
  }
  .contact-list {
    position: absolute;
    left: 236px;
    top: 186px;
    list-style: none;
    font-family: "Arimo", Arial, sans-serif;
    font-size: 15px;
    line-height: 21px;
    color: var(--ink-white);
  }

  /* Front of card */
  .card--front .rose-field {
    position: absolute;
    inset: 0;
    background:
      radial-gradient(ellipse at 70% 70%, var(--rose-light) 0%, transparent 55%),
      radial-gradient(ellipse at 90% 20%, var(--rose-mid) 0%, transparent 60%),
      linear-gradient(135deg, var(--rose-mid) 0%, var(--rose-deep) 100%);
  }
  .card--front .bloom {
    position: absolute;
    left: 10px;
    top: -40px;
    width: 270px;
    height: 270px;
    border-radius: 50%;
    background: radial-gradient(circle at 55% 40%, var(--bloom-red) 0%, #cf1443 55%, var(--bloom-dark) 100%);
  }
  .brand {
    position: absolute;
    left: 250px;
    top: 108px;
    width: 280px;
    text-align: center;
    color: var(--ink-white);
  }
  .brand-rule {
    display: block;
    width: 100%;
    height: 14px;
  }
  .brand-name {
    font-family: "Lobster", cursive;
    font-size: 30px;
    line-height: 1.3;
    font-weight: 400;
    padding: 4px 0;
  }
</style>
</head>
<body>
  <main class="sheet">
    <section class="card card--back" aria-label="Back of business card">
      <div class="bloom" role="img" aria-label="Close-up red paper flower illustration"></div>
      <p class="contact-name">Rosalind Mae</p>
      <ul class="contact-list">
        <li>phone 1300 45 61 27</li>
        <li>mobile 0412 905 738</li>
        <li>info@Rosalindmae.com.au.</li>
      </ul>
    </section>

    <section class="card card--front" aria-label="Front of business card">
      <div class="rose-field" role="img" aria-label="Close-up photograph of pink rose petals"></div>
      <div class="bloom" role="img" aria-label="Red paper flower illustration"></div>
      <div class="brand">
        <svg class="brand-rule" viewBox="0 0 280 14" aria-hidden="true">
          <line x1="0" y1="12" x2="280" y2="12" stroke="#ffffff" stroke-width="1.5"/>
        </svg>
        <h1 class="brand-name">Rosalind Mae Design</h1>
        <svg class="brand-rule" viewBox="0 0 280 14" aria-hidden="true">
          <line x1="0" y1="2" x2="280" y2="2" stroke="#ffffff" stroke-width="1.5"/>
        </svg>
      </div>
    </section>
  </main>
</body>
</html>
```